Brook & Thistle Labels*

Hello :) I am needing labels for my herbal tea/petal product. I am a small producer for the local restaurants (edible flowers/micro herbs & dried product). I am hoping to sell the dried product online. It will be sold in batches as it is ready so quite small/boutique and the label needs to be somewhat generic for the range of produce I make.
Feels: no/minimal plastic, product is in a reusable mason jar, we use organic/regenerative principles from soil health to end product. Treading gently on the land. High quality i.e only fresh hand picked leaf tips for the tea.

```html
<!DOCTYPE html>
<html lang="en">
<head>
<meta charset="utf-8">
<title>Brook &amp; Thistle — Jar Label</title>
<link rel="stylesheet" href="https://fonts.googleapis.com/css2?family=Roboto:wght@400;500;700&display=swap">
<style>
  :root {
    --backdrop: #f4f2ee;
    --kraft: #c8b79d;
    --kraft-light: #d2c3aa;
    --kraft-dark: #b9a688;
    --fibre-dark: rgba(120, 96, 70, 0.22);
    --fibre-light: rgba(236, 226, 208, 0.35);
    --brand-green: #4caf5a;
    --leaf-green: #3f9e4d;
    --leaf-green-soft: #5db66a;
    --ink: #3a3a3a;
    --ink-soft: #4a4845;
  }
  * { box-sizing: border-box; margin: 0; padding: 0; }
  html, body {
    width: 1200px;
    height: 1200px;
    overflow: hidden;
    background: var(--backdrop);
    font-family: "Roboto", Arial, sans-serif;
  }
  .canvas {
    position: relative;
    width: 1200px;
    height: 1200px;
  }
  .label {
    position: absolute;
    left: 272px;
    top: 52px;
    width: 655px;
    height: 1096px;
    overflow: hidden;
    background:
      radial-gradient(circle, var(--fibre-dark) 0 1.2px, transparent 1.8px) 0 0 / 37px 41px,
      radial-gradient(circle, var(--fibre-dark) 0 0.9px, transparent 1.5px) 13px 22px / 53px 47px,
      radial-gradient(circle, var(--fibre-light) 0 1.4px, transparent 2px) 7px 9px / 29px 61px,
      repeating-linear-gradient(33deg, rgba(255,255,255,0.04) 0 2px, rgba(0,0,0,0.025) 2px 5px),
      radial-gradient(ellipse at 20% 15%, var(--kraft-light) 0%, transparent 55%),
      radial-gradient(ellipse at 75% 45%, rgba(210,195,170,0.6) 0%, transparent 45%),
      radial-gradient(ellipse at 85% 90%, var(--kraft-dark) 0%, transparent 55%),
      radial-gradient(ellipse at 10% 70%, rgba(185,166,136,0.7) 0%, transparent 40%),
      var(--kraft);
  }
  .brand-mark {
    position: absolute;
    left: 214px;
    top: 65px;
    width: 226px;
    height: 226px;
    border-radius: 50%;
    background: var(--brand-green);
  }
  .brand-name {
    position: absolute;
    left: 0;
    width: 100%;
    top: 296px;
    text-align: center;
    font-weight: 700;
    font-size: 74px;
    letter-spacing: -0.5px;
    line-height: 1;
    color: var(--ink);
  }
  .product-name {
    position: absolute;
    left: 0;
    width: 100%;
    top: 462px;
    text-align: center;
    color: var(--ink);
    line-height: 1;
  }
  .product-name .primary {
    display: block;
    font-weight: 500;
    font-size: 100px;
  }
  .product-name .secondary {
    display: block;
    margin-top: 4px;
    font-weight: 400;
    font-size: 46px;
    letter-spacing: 1px;
    color: var(--ink-soft);
  }
  .leaf-art {
    position: absolute;
    left: 0;
    top: 784px;
    width: 294px;
    height: 246px;
    border-radius: 0 140px 0 0;
    background: linear-gradient(135deg, var(--leaf-green-soft) 0%, var(--leaf-green) 70%);
    opacity: 0.9;
  }
  .provenance {
    position: absolute;
    left: 40px;
    right: 0;
    top: 1040px;
    text-align: center;
    font-size: 20px;
    line-height: 1.2;
    color: var(--ink-soft);
  }
</style>
</head>
<body>
  <main class="canvas">
    <section class="label">
      <div class="brand-mark"></div>
      <p class="brand-name">Fernwood</p>
      <h1 class="product-name">
        <span class="primary">Brook</span>
        <span class="secondary">&amp; Thistle</span>
      </h1>
      <div class="leaf-art" role="img" aria-label="Green leafy sprig illustration rising from the lower left edge"></div>
      <p class="provenance">Grown, harvested and dried<br>Chemical free on our farm in east Gippsland</p>
    </section>
  </main>
</body>
</html>
```